Labels for an activated Charcoal Facial Wash, Scrub and Mask

We need a new label design for a new line of Facial products. The product, falls under our Brand Lumivo and is based on Activated Charcoal. Activated Black Charcoal Facial wash (250ml), Activated Black Charcoal Mask (100gms) and Activated Black Charcoal face scrub (100gms). We would like to see designs that are modern, clean and must communicate natural products.

```html
<!DOCTYPE html>
<html lang="en">
<head>
<meta charset="UTF-8">
<title>Lumivo Mask Labels</title>
<link href="https://fonts.googleapis.com/css2?family=Marcellus&display=swap" rel="stylesheet">
<style>
  :root{
    --olive:#5e5b4d;
    --gold:#d7cfa6;
    --gold-line:#ccc49a;
    --paper:#ffffff;
    --frame:#3a3a3a;
    --leaf-soft:#cfe3bd;
    --leaf-pale:#eef5e6;
    --pellet-light:#f4f4f4;
    --pellet-mid:#d6d6d6;
    --pellet-dark:#c2c2c2;
  }
  *{margin:0;padding:0;box-sizing:border-box}
  html,body{width:1200px;height:1199px;overflow:hidden;background:var(--paper)}
  .canvas{position:relative;width:1200px;height:1199px;border:1px solid var(--frame);background:var(--paper);font-family:"Marcellus",serif}
  .label{position:absolute;top:139px;width:435px;height:920px;background:var(--paper);overflow:hidden}
  .label--left{left:127px}
  .label--right{left:638px}
  .band-top{position:absolute;left:0;top:0;width:100%;height:68px;background:var(--olive)}
  .band-top .stripe{position:absolute;left:0;top:57px;width:100%;height:4px;background:var(--gold-line)}
  .band-top .foliage{position:absolute;left:0;top:0;width:290px;height:56px}
  .bamboo{position:absolute;left:104px;top:68px;width:331px;height:158px}
  .brand-box{position:absolute;left:50%;transform:translateX(-50%);width:248px;height:177px;border:2px solid var(--gold)}
  .label--left .brand-box{top:187px}
  .label--right .brand-box{top:210px}
  .brand-name{position:absolute;left:0;right:0;bottom:10px;text-align:center;font-size:33px;letter-spacing:11px;padding-left:11px;color:var(--olive);line-height:1}
  .product{position:absolute;left:0;width:100%;text-align:center;color:var(--olive)}
  .label--left .product{top:405px}
  .label--right .product{top:427px}
  .product-title{font-size:84px;line-height:1;font-weight:400;letter-spacing:1px;-webkit-text-stroke:2px var(--olive)}
  .product-sub{margin-top:12px;font-size:31px;line-height:37px}
  .pellets{position:absolute;left:0;top:623px;width:100%;height:229px}
  .band-bottom{position:absolute;left:0;bottom:0;width:100%;height:69px;background:var(--olive)}
  .band-bottom .rule{position:absolute;top:32px;height:3px;background:var(--gold-line)}
  .band-bottom .rule--l{left:0;width:158px}
  .band-bottom .rule--r{right:0;width:165px}
  .band-bottom .foliage{position:absolute;right:0;top:0;width:160px;height:69px}
  .net{position:absolute;left:0;right:0;top:14px;text-align:center;font-size:33px;color:var(--gold);line-height:1}
</style>
</head>
<body>
<div class="canvas">

  <section class="label label--left">
    <div class="band-top">
      <svg class="foliage" role="img" aria-label="Faint leaf line ornament" viewBox="0 0 290 56" preserveAspectRatio="none">
        <defs><linearGradient id="leafTop" x1="0" x2="1"><stop offset="0" stop-color="#6e6a57"/><stop offset="1" stop-color="#5e5b4d"/></linearGradient></defs>
        <rect width="290" height="56" fill="url(#leafTop)"/>
      </svg>
      <div class="stripe"></div>
    </div>
    <div class="brand-box"><div class="brand-name">LUMIVO</div></div>
    <div class="product">
      <h1 class="product-title">MASK</h1>
      <p class="product-sub">with activated<br>black carbon</p>
    </div>
    <svg class="pellets" role="img" aria-label="Photo of activated charcoal pellets" viewBox="0 0 435 229" preserveAspectRatio="none">
      <defs><linearGradient id="pelletL" x1="0" y1="0" x2="0" y2="1"><stop offset="0" stop-color="#ffffff"/><stop offset=".3" stop-color="#f4f4f4"/><stop offset=".7" stop-color="#d6d6d6"/><stop offset="1" stop-color="#c2c2c2"/></linearGradient></defs>
      <rect width="435" height="229" fill="url(#pelletL)"/>
    </svg>
    <div class="band-bottom">
      <svg class="foliage" role="img" aria-label="Faint leaf line ornament" viewBox="0 0 160 69" preserveAspectRatio="none">
        <defs><linearGradient id="leafBot" x1="0" x2="1"><stop offset="0" stop-color="#5e5b4d"/><stop offset="1" stop-color="#6a6654"/></linearGradient></defs>
        <rect width="160" height="69" fill="url(#leafBot)"/>
      </svg>
      <div class="rule rule--l"></div>
      <div class="rule rule--r"></div>
      <div class="net">100 g</div>
    </div>
  </section>

  <section class="label label--right">
    <div class="band-top"><div class="stripe"></div></div>
    <svg class="bamboo" role="img" aria-label="Photo of green bamboo leaves" viewBox="0 0 331 158" preserveAspectRatio="none">
      <defs><linearGradient id="bambooG" x1="1" y1="0" x2="0" y2="1"><stop offset="0" stop-color="#cfe3bd"/><stop offset="1" stop-color="#ffffff"/></linearGradient></defs>
      <rect width="331" height="158" fill="url(#bambooG)"/>
    </svg>
    <div class="brand-box"><div class="brand-name">LUMIVO</div></div>
    <div class="product">
      <h1 class="product-title">MASK</h1>
      <p class="product-sub">with activated<br>black carbon</p>
    </div>
    <svg class="pellets" role="img" aria-label="Photo of activated charcoal pellets" viewBox="0 0 435 229" preserveAspectRatio="none">
      <defs><linearGradient id="pelletR" x1="0" y1="0" x2="0" y2="1"><stop offset="0" stop-color="#ffffff"/><stop offset=".3" stop-color="#f4f4f4"/><stop offset=".7" stop-color="#d6d6d6"/><stop offset="1" stop-color="#c2c2c2"/></linearGradient></defs>
      <rect width="435" height="229" fill="url(#pelletR)"/>
    </svg>
    <div class="band-bottom">
      <div class="rule rule--l"></div>
      <div class="rule rule--r"></div>
      <div class="net">100 g</div>
    </div>
  </section>

</div>
</body>
</html>
```